Sales sheet for printing and embroidery apparel items - Copper Fern Prints

I would like a one page flyer or sales sheet that I would use as a template to send different images of apparel we produce. I have attached examples of layouts I like.
- Ideally, it would have space for 3-5 items.
- I would like it one page only - not a folding flyer.
- Our companies name is Copper Fern Prints.
- This will be used for many different products and markets so I don't need wording/copy. You can use wording from the 7Q7 or K81 flyer.

Colors
0054AA
0677BA
7BADD7
CADEEF
E8F1F8
00AB8E
00BBA5
67D7C9
C6EFE9
E9F9F6
FFC000
F8CF3A
FAE287
FDF2CF
FEFAEE

Requirements
Must have
• Places for between 3 and 5 images of apparel (t-shirts, hats etc)

```html
<!DOCTYPE html>
<html lang="en">
<head>
<meta charset="utf-8">
<title>Copper Fern Prints – Sample Merch Kit</title>
<link rel="stylesheet" href="https://fonts.googleapis.com/css2?family=Barlow:ital,wght@0,400;0,500;0,600;0,700;1,500&family=Barlow+Semi+Condensed:wght@500;700&family=Inter:wght@800&display=swap">
<style>
  :root{
    --sky:#cdecf0;
    --navy:#173f7f;
    --photo-deep:#1b4a8c;
    --photo-light:#2d62a8;
    --coral:#ee5a5a;
    --orange:#ee7a2c;
    --teal-dark:#2f6d68;
    --teal-light:#69b6c0;
    --hatch:#444b52;
    --ink:#4f5357;
    --bright-blue:#2f8fe0;
    --series-blue:#2f8fe6;
    --frame:#2b6468;
    --page:#ececec;
    --white:#ffffff;
  }
  *{box-sizing:border-box;margin:0;padding:0}
  html,body{width:1200px;height:1200px;overflow:hidden;background:var(--page)}
  body{font-family:"Barlow",sans-serif;position:relative}
  .sheet{
    position:absolute;left:0;top:0;width:1210px;height:1566px;
    transform-origin:0 0;
    transform:translate(136.5px,0) scale(0.7663);
    background:var(--white);overflow:hidden;
  }
  .sheet > *{position:absolute}
  .backdrop{left:0;top:0;width:1210px;height:1566px}
  .brand{
    left:0;width:1210px;top:78px;text-align:center;
    font-family:"Barlow",sans-serif;font-weight:700;font-size:46px;
    letter-spacing:2px;color:var(--navy);white-space:nowrap;
  }
  .title{
    left:0;width:1210px;top:300px;text-align:center;
    font-family:"Inter",sans-serif;font-weight:800;font-size:80px;
    letter-spacing:-2px;color:var(--white);line-height:1;white-space:nowrap;
  }
  .tags{left:256px;top:386px;display:flex;height:33px}
  .tag{
    font-family:"Barlow Semi Condensed",sans-serif;font-weight:500;font-size:21px;color:var(--white);
    display:flex;align-items:center;justify-content:center;white-space:nowrap;
    clip-path:polygon(10px 0,100% 0,calc(100% - 10px) 100%,0 100%);
  }
  .tag-model{background:var(--orange);width:296px}
  .tag-series{background:var(--series-blue);width:408px;margin-left:-5px}
  .warning{
    left:0;width:1210px;top:430px;text-align:center;color:var(--white);
    font-style:italic;font-weight:500;font-size:15px;line-height:19px;
  }
  .shirt{height:300px;top:477px;
    clip-path:polygon(22% 0,78% 0,100% 18%,88% 35%,80% 30%,80% 100%,20% 100%,20% 30%,12% 35%,0 18%)}
  .shirt-olive{left:137px;width:310px;background:linear-gradient(#655e48,#57503c)}
  .shirt-black{left:487px;width:310px;background:linear-gradient(#1c1c1c,#0b0b0b)}
  .shirt-royal{left:830px;width:315px;background:linear-gradient(#3342a8,#283793)}
  .shadow{top:776px;height:14px;border-radius:50%;
    background:radial-gradient(ellipse at center,rgba(0,0,0,.25),rgba(0,0,0,0) 70%)}
  .contents{
    left:70px;top:808px;width:1062px;height:207px;
    border:2px solid var(--frame);border-radius:20px;
  }
  .contents-title{
    left:0;width:1210px;top:820px;text-align:center;color:var(--coral);
    font-weight:700;font-size:37px;
  }
  .kit-item{top:880px;display:flex;align-items:center;gap:22px}
  .kit-icon{width:104px;height:104px;border-radius:50%;background:var(--sky);
    display:flex;align-items:center;justify-content:center}
  .kit-label{font-weight:600;font-size:27px;line-height:34px;color:var(--ink);white-space:nowrap}
  .cap{width:175px;height:140px;border-radius:90px 90px 14px 14px}
  .cap-red{left:102px;top:1055px;background:linear-gradient(#e54a4e,#b7252c)}
  .cap-green{left:322px;top:1055px;background:linear-gradient(#9ee04d,#5fa81e)}
  .cap-blue{left:102px;top:1225px;background:linear-gradient(#4ea6ea,#2b78c2)}
  .cap-gray{left:322px;top:1225px;background:linear-gradient(#6b6b6b,#3d3d3d)}
  .order-title{left:546px;top:1078px;color:var(--navy);font-weight:700;font-size:39px;white-space:nowrap}
  .step{left:550px;display:flex;align-items:center;gap:18px;
    font-weight:500;font-size:39px;color:var(--ink);white-space:nowrap}
  .step svg{width:62px;height:62px}
  .footer-phone{left:55px;top:1470px;display:flex;align-items:center;gap:10px;
    font-weight:700;font-size:58px;color:var(--white);white-space:nowrap}
  .footer-mail{left:485px;top:1480px;display:flex;gap:6px;color:var(--white);
    font-size:19px;line-height:25px;font-weight:500;white-space:nowrap}
  .footer-web{right:32px;top:1491px;display:flex;align-items:center;gap:10px;
    font-family:"Barlow Semi Condensed",sans-serif;font-weight:700;font-size:26px;
    color:var(--white);white-space:nowrap}
</style>
</head>
<body>
<main class="sheet">
  <svg class="backdrop" viewBox="0 0 1210 1566" aria-hidden="true">
    <rect x="0" y="0" width="1210" height="680" fill="var(--sky)"/>
    <g stroke="var(--hatch)" stroke-width="4">
      <line x1="209" y1="157" x2="0" y2="366"/><line x1="195" y1="157" x2="0" y2="352"/>
      <line x1="181" y1="157" x2="0" y2="338"/><line x1="167" y1="157" x2="0" y2="324"/>
      <line x1="153" y1="157" x2="0" y2="310"/><line x1="139" y1="157" x2="0" y2="296"/>
      <line x1="125" y1="157" x2="0" y2="282"/><line x1="111" y1="157" x2="0" y2="268"/>
      <line x1="97" y1="157" x2="0" y2="254"/><line x1="83" y1="157" x2="0" y2="240"/>
      <line x1="1001" y1="157" x2="1210" y2="366"/><line x1="1015" y1="157" x2="1210" y2="352"/>
      <line x1="1029" y1="157" x2="1210" y2="338"/><line x1="1043" y1="157" x2="1210" y2="324"/>
      <line x1="1057" y1="157" x2="1210" y2="310"/><line x1="1071" y1="157" x2="1210" y2="296"/>
      <line x1="1085" y1="157" x2="1210" y2="282"/><line x1="1099" y1="157" x2="1210" y2="268"/>
      <line x1="1113" y1="157" x2="1210" y2="254"/><line x1="1127" y1="157" x2="1210" y2="240"/>
    </g>
    <polygon points="0,500 250,250 960,250 1210,500 1210,680 0,680" fill="var(--white)"/>
    <g fill="none" stroke-width="20" stroke-linejoin="miter">
      <polyline stroke="var(--coral)" points="0,387 217,170 993,170 1210,387"/>
      <polyline stroke="var(--orange)" points="0,415 225,190 985,190 1210,415"/>
      <polyline stroke="var(--teal-dark)" points="0,443 233,210 977,210 1210,443"/>
      <polyline stroke="var(--teal-light)" points="0,472 242,230 968,230 1210,472"/>
    </g>
    <defs>
      <linearGradient id="photoTone" x1="0" y1="0" x2="0" y2="1">
        <stop offset="0" stop-color="var(--photo-deep)"/>
        <stop offset="1" stop-color="var(--photo-light)"/>
      </linearGradient>
    </defs>
    <polygon role="img" aria-label="Faded blue-toned photo of the print shop team at work"
      points="0,517 262,255 948,255 1210,517 1210,665 0,665" fill="url(#photoTone)"/>
    <rect x="0" y="665" width="1210" height="15" fill="var(--white)"/>
    <path d="M0 1430 C60 1410 120 1425 190 1400 L240 1440 C300 1405 380 1420 430 1395 C480 1380 520 1405 560 1392 L600 1430 C680 1410 760 1395 840 1400 C900 1402 960 1420 1020 1395 C1080 1380 1150 1385 1210 1380 L1210 1566 L0 1566 Z" fill="var(--photo-deep)"/>
    <path d="M0 1445 C70 1430 130 1445 190 1425 L240 1460 C300 1428 380 1440 430 1418 C480 1405 520 1428 560 1416 L600 1452 C680 1432 760 1420 840 1424 C900 1426 960 1442 1020 1420 C1080 1406 1150 1410 1210 1405 L1210 1566 L0 1566 Z" fill="var(--bright-blue)"/>
  </svg>

  <div class="brand">COPPER FERN PRINTS</div>
  <h1 class="title">SAMPLE MERCH KIT</h1>
  <div class="tags">
    <span class="tag tag-model">MODEL: CFP SHOP T-SHIRTS</span>
    <span class="tag tag-series">SERIES: SUMMER/FALL 2025 COLLECTION</span>
  </div>
  <p class="warning">WARNING:&nbsp; These shirts may cause increased shop morale, envy from<br>competitors, and a high volume of customer demand.</p>

  <div class="shirt shirt-olive" role="img" aria-label="Olive t-shirt printed with a Hollis Equipment vintage truck graphic"></div>
  <div class="shirt shirt-black" role="img" aria-label="Black t-shirt printed with a North Shore Trail off-road truck graphic"></div>
  <div class="shirt shirt-royal" role="img" aria-label="Royal blue t-shirt printed with a Harbor Lane Drive muscle car graphic"></div>
  <div class="shadow" style="left:150px;width:290px"></div>
  <div class="shadow" style="left:500px;width:290px"></div>
  <div class="shadow" style="left:845px;width:290px"></div>

  <div class="contents"></div>
  <h2 class="contents-title">MERCH KIT CONTENTS:</h2>
  <div class="kit-item" style="left:101px">
    <div class="kit-icon">
      <svg width="60" height="60" viewBox="0 0 60 60" fill="none" stroke="var(--navy)" stroke-width="2.5" stroke-linejoin="round"><path d="M22 8 L8 16 L13 28 L18 26 L18 52 L42 52 L42 26 L47 28 L52 16 L38 8 C36 13 24 13 22 8 Z"/></svg>
    </div>
    <div class="kit-label">Custom Shop<br>T-shirt</div>
  </div>
  <div class="kit-item" style="left:460px">
    <div class="kit-icon">
      <svg width="60" height="60" viewBox="0 0 60 60" fill="none" stroke="var(--navy)" stroke-width="2.5" stroke-linejoin="round"><path d="M20 14 L6 21 L11 32 L16 30 L16 54 L40 54 L40 30 L45 32 L50 21 L36 14 C34 19 22 19 20 14 Z"/><path d="M28 30 L30 36 L36 38 L30 40 L28 46 L26 40 L20 38 L26 36 Z"/><path d="M48 4 L49.5 8.5 L54 10 L49.5 11.5 L48 16 L46.5 11.5 L42 10 L46.5 8.5 Z"/></svg>
    </div>
    <div class="kit-label">Additional<br>Sample Shirt</div>
  </div>
  <div class="kit-item" style="left:811px">
    <div class="kit-icon">
      <svg width="60" height="60" viewBox="0 0 60 60" fill="none" stroke="var(--navy)" stroke-width="2.5" stroke-linejoin="round"><rect x="6" y="24" width="8" height="16"/><path d="M14 26 L28 20 L44 30 L40 38 L14 38"/><path d="M20 8 L54 50 L50 54 L16 12 Z"/></svg>
    </div>
    <div class="kit-label">CFP Ink<br>Pen</div>
  </div>

  <div class="cap cap-red" role="img" aria-label="Red baseball cap"></div>
  <div class="cap cap-green" role="img" aria-label="Lime green baseball cap"></div>
  <div class="cap cap-blue" role="img" aria-label="Sky blue baseball cap"></div>
  <div class="cap cap-gray" role="img" aria-label="Charcoal baseball cap"></div>

  <h2 class="order-title">HOW TO START AN ORDER</h2>
  <div class="step" style="top:1130px">
    <svg viewBox="0 0 60 60" fill="none" stroke="#222" stroke-width="2.5"><circle cx="34" cy="26" r="20"/><line x1="20" y1="40" x2="6" y2="54"/><rect x="24" y="22" width="20" height="9" rx="2"/><circle cx="28" cy="33" r="3"/><circle cx="40" cy="33" r="3"/></svg>
    <span>Choose Your Ride</span>
  </div>
  <div class="step" style="top:1216px">
    <svg viewBox="0 0 60 60" fill="none" stroke="#222" stroke-width="2.5" stroke-linejoin="round"><path d="M22 6 L8 14 L13 24 L18 22 L18 52 L42 52 L42 22 L47 24 L52 14 L38 6 C36 11 24 11 22 6 Z"/><path d="M28 48 L28 32 C28 29 32 29 32 32 L32 40 L38 41 C41 42 41 45 40 48"/></svg>
    <span>Pick Your Gear</span>
  </div>
  <div class="step" style="top:1303px">
    <svg viewBox="0 0 60 60" fill="none" stroke="#222" stroke-width="2.5" stroke-linejoin="round"><path d="M10 50 L36 24 M44 8 C38 8 34 14 36 20 L30 26 L34 30 L40 24 C46 26 52 22 52 16 L46 18 L42 14 Z"/><path d="M12 12 L18 8 L48 42 L52 52 L42 48 Z"/></svg>
    <span>We Customize</span>
  </div>

  <div class="footer-phone">
    <svg width="44" height="56" viewBox="0 0 44 56" fill="var(--white)"><path d="M14 4 C6 8 4 18 6 30 C8 42 14 50 22 52 L28 46 L22 36 L16 38 C12 32 12 22 14 18 L20 16 L20 4 Z"/></svg>
    <span>555-014-2273</span>
  </div>
  <div class="footer-mail">
    <svg width="20" height="14" viewBox="0 0 20 14" fill="none" stroke="var(--white)" stroke-width="1.8" style="margin-top:5px"><rect x="1" y="1" width="18" height="12"/><polyline points="1,1 10,8 19,1"/></svg>
    <span>For more information, email us at<br>hello@copperfernprints.com</span>
  </div>
  <div class="footer-web">
    <svg width="26" height="26" viewBox="0 0 26 26" fill="none" stroke="var(--white)" stroke-width="2"><circle cx="13" cy="13" r="11"/><ellipse cx="13" cy="13" rx="5" ry="11"/><line x1="2" y1="13" x2="24" y2="13"/><line x1="4" y1="7" x2="22" y2="7"/><line x1="4" y1="19" x2="22" y2="19"/></svg>
    <span>WWW.COPPERFERNPRINTS.COM</span>
  </div>
</main>
</body>
</html>
```